Brenmoor Group needs a business card

I would like the card to be simple but modern and elegant.
I like black and white.
or black and gold.
we are a private finance lender and also are involved in property and property developments.

please look at the business card photos i provided i would like B.G only one one side and all the other details on the other side use fonts that tie in with my theme.

Industry/Entity Type

Finance

Contact Information for Business Card

Brenmoor Group (B.G) Callum Brenmoor M: 0418396152 E: callumbren@quivomail.com

Font styles to use
Other font styles liked:
• Use fonts that would reflect our business

Colors
000000
ffffff

Requirements
Must have
• one side of details
• other side has either B.G or Brenmoor Group like in the photos provided

```html
<!DOCTYPE html>
<html lang="en">
<head>
<meta charset="utf-8">
<title>Brenmoor Group — Business Card</title>
<link rel="stylesheet" href="https://fonts.googleapis.com/css2?family=Open+Sans:wght@400;700&display=swap">
<style>
  :root {
    --ink: #000000;
    --paper: #ffffff;
    --backdrop: #d9d7d6;
    --rule: #1a1a1a;
  }
  * { margin: 0; padding: 0; box-sizing: border-box; }
  html, body {
    width: 1200px;
    height: 1011px;
    overflow: hidden;
    background: var(--backdrop);
    font-family: "Open Sans", Arial, sans-serif;
  }
  .stage {
    position: relative;
    width: 1200px;
    height: 1011px;
  }
  .card {
    position: absolute;
    left: 250px;
    width: 700px;
    height: 400px;
    box-shadow: 0 12px 28px rgba(0,0,0,0.18);
  }
  .card--front {
    top: 70px;
    background: var(--ink);
    display: flex;
    align-items: center;
    justify-content: center;
  }
  .front-name {
    font-family: "Open Sans", Arial, sans-serif;
    font-weight: 400;
    color: var(--paper);
    font-size: 44px;
    letter-spacing: 3px;
    line-height: 1;
  }
  .card--back {
    top: 540px;
    background: var(--paper);
    color: var(--ink);
  }
  .card__lines {
    position: absolute;
    inset: 0;
  }
  .brand {
    position: absolute;
    left: 48px;
    top: 236px;
    font-weight: 700;
    font-size: 26px;
    color: var(--ink);
  }
  .holder {
    position: absolute;
    left: 330px;
    top: 150px;
  }
  .holder__name {
    font-size: 34px;
    font-weight: 400;
    letter-spacing: 1px;
    margin-bottom: 14px;
  }
  .contact {
    list-style: none;
    margin-left: 60px;
  }
  .contact__item {
    display: flex;
    align-items: center;
    gap: 10px;
    font-size: 17px;
    margin-bottom: 8px;
  }
  .contact__icon {
    width: 20px;
    height: 20px;
    flex: none;
  }
</style>
</head>
<body>
<main class="stage">
  <section class="card card--front" aria-label="Card front">
    <span class="front-name">Brenmoor Group</span>
  </section>

  <section class="card card--back" aria-label="Card back">
    <svg class="card__lines" viewBox="0 0 700 400" aria-hidden="true">
      <line x1="600" y1="22" x2="555" y2="130" stroke="var(--rule)" stroke-width="1.5"/>
      <line x1="378" y1="290" x2="335" y2="390" stroke="var(--rule)" stroke-width="1.5"/>
    </svg>

    <div class="brand">Brenmoor Group</div>

    <div class="holder">
      <h1 class="holder__name">Callum Brenmoor</h1>
      <ul class="contact">
        <li class="contact__item">
          <svg class="contact__icon" viewBox="0 0 20 20" aria-label="Mobile">
            <rect width="20" height="20" rx="4" fill="var(--ink)"/>
            <rect x="6.5" y="3.5" width="7" height="13" rx="1.2" fill="none" stroke="var(--paper)" stroke-width="1.5"/>
            <circle cx="10" cy="14" r="0.9" fill="var(--paper)"/>
          </svg>
          <span>0418396152</span>
        </li>
        <li class="contact__item">
          <svg class="contact__icon" viewBox="0 0 20 20" aria-label="Email">
            <rect width="20" height="20" rx="4" fill="var(--ink)"/>
            <rect x="4" y="6" width="12" height="8.5" fill="none" stroke="var(--paper)" stroke-width="1.4"/>
            <polyline points="4,6 10,11 16,6" fill="none" stroke="var(--paper)" stroke-width="1.4"/>
          </svg>
          <span>callumbren@quivomail.com</span>
        </li>
      </ul>
    </div>
  </section>
</main>
</body>
</html>
```